fizzy drinks label design

I want to design fizzy drink label for 3 flavors : black grapes, red apple and mojito, band name kestrola, product name KOLTA , product will be in plastic bottle, label size 198 mm X 66mm

```html
<!DOCTYPE html>
<html lang="en">
<head>
<meta charset="utf-8">
<title>KOLTA fizzy drink labels</title>
<link rel="stylesheet" href="https://fonts.googleapis.com/css2?family=Oswald:wght@500;600;700&display=swap">
<style>
  :root {
    --page: #eef1f3;
    --sky-top: #1d6fc4;
    --sky-mid: #4fa6e6;
    --sky-low: #bfe3f7;
    --leaf: #3f7d4a;
    --brand: #f07a1c;
    --ink-white: #ffffff;
    --band: #ffffff;
    --maker: #2e6b2f;
    --rule: #2e6b2f;
    --tag-apple: #8e1f2b;
    --tag-mojito: #3d6b1e;
    --tag-grape: #5a1747;
    --text-dark: #333333;
  }
  * { box-sizing: border-box; margin: 0; padding: 0; }
  html, body { width: 1200px; height: 878px; overflow: hidden; }
  body {
    background: var(--page);
    font-family: "Oswald", "Arial Narrow", sans-serif;
    position: relative;
  }
  .range {
    position: absolute;
    left: 100px;
    top: 40px;
    display: flex;
    gap: 35px;
  }
  .flavour {
    width: 310px;
    display: flex;
    flex-direction: column;
    align-items: center;
  }
  .neck-tag {
    width: 50px;
    height: 150px;
    background: var(--band);
    border-radius: 0 0 25px 25px;
    box-shadow: 0 1px 3px rgba(0,0,0,.15);
    display: flex;
    align-items: center;
    justify-content: center;
    margin-bottom: 18px;
  }
  .neck-tag span {
    transform: rotate(-90deg);
    white-space: nowrap;
    font-weight: 600;
    font-size: 20px;
    letter-spacing: .5px;
  }
  .apple .neck-tag span { color: var(--tag-apple); }
  .mojito .neck-tag span { color: var(--tag-mojito); }
  .grape .neck-tag span { color: var(--tag-grape); }

  .label {
    width: 310px;
    height: 600px;
    border-radius: 6px;
    overflow: hidden;
    position: relative;
    box-shadow: 0 4px 14px rgba(0,0,0,.18);
    background: linear-gradient(180deg, var(--sky-top) 0%, var(--sky-mid) 38%, var(--sky-low) 62%, #ffffff 78%);
  }
  .leaves {
    position: absolute;
    top: 0; left: 0; right: 0;
    height: 150px;
    background:
      radial-gradient(ellipse 90px 130px at 0% 10%, rgba(63,125,74,.75), transparent 70%),
      radial-gradient(ellipse 90px 130px at 100% 10%, rgba(63,125,74,.75), transparent 70%);
  }
  .brand {
    position: absolute;
    top: 84px;
    width: 100%;
    text-align: center;
    font-weight: 700;
    font-size: 46px;
    color: var(--brand);
    letter-spacing: 1px;
  }
  .flavour-name {
    position: absolute;
    top: 160px;
    width: 100%;
    text-align: center;
    font-weight: 600;
    font-size: 44px;
    color: var(--ink-white);
    letter-spacing: .5px;
  }
  .fruit {
    position: absolute;
    top: 255px;
    left: 0; right: 0;
    height: 220px;
  }
  .apple .fruit { background: radial-gradient(ellipse at 50% 55%, #f3d9c4 0%, #c22b33 45%, #7d1820 80%, transparent 100%); }
  .mojito .fruit { background: radial-gradient(ellipse at 50% 55%, #d9f29a 0%, #6fc13a 45%, #2f7d1e 80%, transparent 100%); }
  .grape .fruit { background: radial-gradient(ellipse at 50% 55%, #9b5a8a 0%, #5e2150 50%, #3a1232 80%, transparent 100%); }

  .base-band {
    position: absolute;
    left: 0; right: 0; bottom: 0;
    height: 125px;
    background: var(--band);
  }
  .maker {
    position: absolute;
    left: 16px;
    top: 40px;
    display: flex;
    align-items: center;
    gap: 6px;
    font-weight: 600;
    font-size: 22px;
    color: var(--maker);
  }
  .maker i {
    display: block;
    width: 12px; height: 12px;
    background: var(--maker);
  }
  .volume {
    position: absolute;
    right: 18px;
    top: 30px;
    font-weight: 500;
    font-size: 18px;
    color: var(--text-dark);
  }
  .rule {
    position: absolute;
    left: 130px; right: 16px;
    top: 66px;
    height: 3px;
    background: var(--rule);
  }
</style>
</head>
<body>
  <main class="range">
    <section class="flavour apple">
      <div class="neck-tag"><span>RED APPLE</span></div>
      <div class="label">
        <div class="leaves" role="img" aria-label="Palm leaves hanging into the top corners"></div>
        <div class="brand">KOLTA</div>
        <h2 class="flavour-name">RED APPLE</h2>
        <div class="fruit" role="img" aria-label="Photo of red apples, one cut in half"></div>
        <div class="base-band">
          <div class="maker"><i></i>kestrola</div>
          <div class="volume">200ml</div>
          <div class="rule"></div>
        </div>
      </div>
    </section>

    <section class="flavour mojito">
      <div class="neck-tag"><span>MOJITO</span></div>
      <div class="label">
        <div class="leaves" role="img" aria-label="Palm leaves hanging into the top corners"></div>
        <div class="brand">KOLTA</div>
        <h2 class="flavour-name">MOJITO</h2>
        <div class="fruit" role="img" aria-label="Photo of whole and sliced green limes"></div>
        <div class="base-band">
          <div class="maker"><i></i>kestrola</div>
          <div class="volume">200ml</div>
          <div class="rule"></div>
        </div>
      </div>
    </section>

    <section class="flavour grape">
      <div class="neck-tag"><span>BLACK GRAPES</span></div>
      <div class="label">
        <div class="leaves" role="img" aria-label="Palm leaves hanging into the top corners"></div>
        <div class="brand">KOLTA</div>
        <h2 class="flavour-name">BLACK GRAPES</h2>
        <div class="fruit" role="img" aria-label="Photo of a bunch of black grapes with a vine leaf"></div>
        <div class="base-band">
          <div class="maker"><i></i>kestrola</div>
          <div class="volume">200ml</div>
          <div class="rule"></div>
        </div>
      </div>
    </section>
  </main>
</body>
</html>
```